Movie poster for short film: TINFOIL

We need a creative, artistic, stylized poster design for our short film TINFOIL. We would like to see designs with graphics and bold colors more than photographs. The photographs we are posting are more for reference- you do not have to use them in the poster! We are looking for something clean and simple. The film is a drama so please don't make it funny. The mood of the film is thoughtful and introspective. Name of film should be in all caps. Things to include in the poster:
Name of film: TINFOIL
Velvet Harbor Pictures
Starring Marisa Calloway

Here is a brief plot synopsis: TINFOIL follows one night in the life of a rebellious young woman who breaks into a diner after hours with a can of spray paint. Her intentions change after she ends up discovering what's left of a love story.

The movie is somewhat experimental, set to music for part of it with no dialog. The whole movie takes place in an old fashioned diner.

Target Market(s)

Film festival attendees between the ages of 20-50

Industry/Entity Type

Movie

Font styles to use
Sans Serif

Requirements
Must have
• See project description above- also the film is somewhat dark in nature so please don't make it too 'happy' looking.

```html
<!DOCTYPE html>
<html lang="en">
<head>
<meta charset="utf-8">
<title>TINFOIL — Poster</title>
<link rel="stylesheet" href="https://fonts.googleapis.com/css2?family=Arimo:wght@400;700&family=Bebas+Neue&display=swap">
<style>
  :root {
    --sky-deep: #081c21;
    --sky-teal: #2c6272;
    --sky-mid: #4f97b4;
    --sky-low: #6cb9dc;
    --glow: #ffffff;
    --title-ink: #ffffff;
    --credit-ink: #0d1418;
    --object-light: #ea2f5c;
    --object-main: #dc1a44;
  }
  html, body {
    margin: 0;
    padding: 0;
    width: 960px;
    height: 1200px;
    overflow: hidden;
  }
  .poster {
    position: relative;
    width: 960px;
    height: 1200px;
    overflow: hidden;
    background:
      radial-gradient(ellipse 520px 340px at 480px 566px,
        var(--glow) 0%, rgba(255,255,255,0.95) 30%, rgba(255,255,255,0.55) 62%, rgba(255,255,255,0) 100%),
      linear-gradient(180deg,
        var(--sky-deep) 0%, var(--sky-teal) 25%, var(--sky-mid) 60%, var(--sky-low) 100%);
    font-family: "Arimo", Arial, sans-serif;
  }
  .title {
    position: absolute;
    top: 190px;
    left: 0;
    width: 100%;
    margin: 0;
    text-align: center;
    color: var(--title-ink);
    font-weight: 700;
    font-size: 51px;
    letter-spacing: 0.2em;
    padding-left: 0.2em;
    box-sizing: border-box;
    line-height: 1;
  }
  .hero-object {
    position: absolute;
    left: 420px;
    top: 510px;
    width: 110px;
    height: 110px;
    background: linear-gradient(135deg, var(--object-light), var(--object-main));
  }
  .credits {
    position: absolute;
    left: 0;
    width: 100%;
    text-align: center;
    color: var(--credit-ink);
    margin: 0;
    line-height: 1;
  }
  .credits--label {
    top: 865px;
    font-size: 19px;
    letter-spacing: 0.06em;
  }
  .credits--star {
    top: 898px;
    font-size: 32px;
    letter-spacing: 0.3em;
    padding-left: 0.3em;
    box-sizing: border-box;
  }
  .credits--studio {
    top: 985px;
    font-family: "Bebas Neue", "Arial Narrow", sans-serif;
    font-size: 33px;
    letter-spacing: 0.01em;
  }
</style>
</head>
<body>
  <main class="poster">
    <h1 class="title">TINFOIL</h1>
    <div class="hero-object" role="img" aria-label="Photograph of a single red gumball resting in a pale pool of light"></div>
    <p class="credits credits--label">STARRING</p>
    <p class="credits credits--star">MARISA CALLOWAY</p>
    <p class="credits credits--studio">VELVET HARBOR PICTURES</p>
  </main>
</body>
</html>
```